Web Design Nutrition supplements (Quilvara 5 pages)

We are looking for templates for a new nutrition supplement shop www.velomira.ch , targeting Swiss Female 65% /Male 35% over 40 yrs with high quality products (no performance enhancement /Body building products).
Our customers are not the most proficient in internet, so the website should be simple, easily understood. not too much web2.0 look and feel and functionality.

velomira.ch product offerings are high quality and supplied from top brands: like Dr. Holtfen, Varoun, talmquist, Nobrafit), for diets, weight management, antistress, anti-apathy, oligo-elements, omega-3 oils, and cosmetics.

We want the website design
1) to reflect our seriousness and expertise in the area,
2)to Inspire trust from our customers and address their needs in a personal and professional way (we answer your questions over email/Phone)
3) though we are not an pharmacy, our products are currently sold in pharmacies in Switzerland, so we want our customers to feel as well served online, as if they were in a pharmacy.
4) compare favorably to international websites (F, G) also selling online to Swiss customers: we are a truly Swiss company and can deliver within less than 18 h. in Switzerland (so the Swiss flag is an important design element for us)

We want to provide a superior buying experience,
1) important: providing sufficient product information: (intelligible snippet/summary of product info) should be visible on search result pages, and category pages,
2) clarity of design "emphasis" on products with clear call to action (buy)

Deliverables for the winning designer;
Photoshop files that can be easily be integrated in our quilvara shop.
- Homepage
- Category Page
- Product Page
For 1st evaluation and corrections of the proposals.

- Landing Page (for SEM Campaigns)
- Newsletter (Post finch)
as a second step.

Please use the attached wireframes, that should give you the exact content we want to provide (as well as functionality), the wireframes donnot define the user experience/design (it s more like a guidance, suggestion)

Target Market(s)

Swiss Males /35% Females 65% (both Swiss French/ Swiss German over 40 years

Industry/Entity Type

Nutrition

Requirements
Must have
• Deliverables:
- Homepage
- Category Page
- Product Page

- Newsletter template
- Landing Page

We attach:
- navigation to show how users can access the products (cat/ sub cat, but also search for body parts, objectives of healing... (see Kategorien-for-web.xls)
- Wireframes (myTrevolin)
- Logo (1 psd)
- Product images (zip files)
- Benchmarks: wellmorrow.co.uk (simplicity), kpv.com (expandable navigation),
- Competitors: ro7.de, talnori.com, talnori-deutschland.de, ultra-keen.eu

```html
<!DOCTYPE html>
<html lang="de">
<head>
<meta charset="utf-8">
<title>Velomira – Nahrungsergänzung</title>
<link href="https://fonts.googleapis.com/css2?family=Open+Sans:wght@400;600;700&family=Oswald:wght@500&family=Tinos:wght@400;700&display=swap" rel="stylesheet">
<style>
:root{
  --page-bg:#e8e8e8;
  --white:#ffffff;
  --slate:#6b869d;
  --slate-dark:#56708a;
  --text:#333333;
  --muted:#7a8a98;
  --grey-band:#d5d5d5;
  --footer:#e3e3e3;
  --line:#b9b9b9;
  --green:#4f8a1c;
  --green-dark:#3c6e12;
  --lime:#6f9b10;
  --gold:#c8b200;
  --red:#e11212;
  --crimson:#c40000;
  --orange-red:#e03a00;
  --pink:#c0398a;
}
*{box-sizing:border-box;margin:0;padding:0}
html,body{width:1136px;height:1200px;overflow:hidden}
body{background:var(--page-bg);font-family:"Open Sans",Verdana,sans-serif;color:var(--text);position:relative}
.page{position:absolute;left:168px;top:11px;width:800px;height:1178px;background:var(--white)}
.abs{position:absolute}

/* header */
.brand{left:14px;top:16px;display:flex;align-items:center;gap:8px}
.brand-mark{width:30px;height:30px;background:var(--lime);border-radius:4px}
.brand-name{font-size:38px;font-weight:400;color:var(--slate);letter-spacing:1px;line-height:1}
.info{font-size:10px;line-height:16px;color:var(--text)}
.vsep{width:1px;height:42px;background:#dcdcdc}
.search{left:280px;top:53px;width:318px;height:23px;border:1px solid #d2d2d2;font-size:10px;color:#888;padding:4px 8px}
.search svg{position:absolute;right:8px;top:5px}
.topright{right:14px;text-align:right;font-size:10px;color:#555}
.topright .items{color:var(--green)}
.flag{display:inline-block;width:13px;height:9px;vertical-align:middle;margin-left:5px}

/* nav */
.nav{left:0;top:88px;width:800px;height:44px;background:var(--slate);border-top:1px solid var(--slate-dark)}
.nav a{position:absolute;top:13px;font-family:"Oswald",sans-serif;font-size:11.5px;color:#fff;text-decoration:none;letter-spacing:.3px}
.nav i{position:absolute;top:12px;width:1px;height:20px;background:#8aa0b3}

/* hero */
.hero{left:0;top:133px;width:800px;height:264px}
.cats{left:0;top:0;width:202px;height:264px;background:linear-gradient(90deg,var(--lime) 0%,#9caa08 60%,var(--gold) 100%)}
.cats h3{position:absolute;left:18px;top:10px;font-size:14px;font-weight:600;color:#3d4a0a;letter-spacing:.5px}
.cats ul{list-style:none;position:absolute;left:18px;top:36px}
.cats li{font-size:10.4px;color:#fff;height:22.4px}
.cats li::before{content:"→ ";font-size:8px}
.slide{left:202px;top:0;width:434px;height:264px;border:1px solid #cfcfcf;background:#fff}
.slide-photo{left:2px;top:0;width:116px;height:262px;background:linear-gradient(180deg,#2d4f9c 0%,#e9eef6 35%,#eef1f6 70%,#1f3f8f 100%)}
.slide h2{left:153px;top:54px;font-size:14px;font-weight:600;color:#222}
.slide p{left:154px;top:81px;width:250px;font-size:10px;line-height:16px;color:#333}
.btn-shop{left:155px;top:157px;width:77px;height:24px;background:var(--red);color:#fff;font-size:10px;text-align:center;line-height:24px;border:1px solid #b00}
.dots{left:161px;top:213px;display:flex;gap:9.5px}
.dots span{width:9px;height:9px;border-radius:50%;background:#c4c4c4;border:1px solid #a9a9a9}
.dots .on{background:var(--green);border-color:var(--green-dark)}
.help{left:638px;top:0;width:162px;height:264px;border:1px solid #cfcfcf;background:#fff;overflow:hidden}
.help-photo{left:0;top:62px;width:120px;height:202px;background:radial-gradient(ellipse at 50% 40%,#e9c9a8 0%,#e6e3df 55%,#f4f4f4 100%)}
.help h3{left:0;width:160px;top:20px;text-align:center;font-family:"Tinos",serif;font-size:19px;font-weight:400;color:#2b3a48}
.phone{left:24px;top:52px;font-family:"Open Sans",sans-serif;font-style:italic;font-weight:700;font-size:26px;line-height:31px;color:#1c2530;text-align:right;width:120px}
.click{left:78px;top:150px;width:73px;height:24px;background:#eef3f7;border:1px solid #c5d3df;color:var(--slate);font-size:10px;text-align:center;line-height:22px}

/* special */
.special{left:0;top:397px;width:800px;height:192px;background:var(--grey-band)}
.sec-title{position:absolute;left:22px;top:14px;font-size:13.6px;font-weight:600;color:#333;letter-spacing:.4px}
.sec-rule{position:absolute;left:10px;width:780px;height:1px;background:var(--line)}
.card{position:absolute;top:59px;width:249px;height:108px;background:#fff;border:1px solid #b5b5b5}
.card .pack{position:absolute;left:6px;top:8px;width:94px;height:92px}
.card h4{position:absolute;left:109px;top:16px;font-size:10.4px;line-height:13px;font-weight:700;width:120px}
.card p{position:absolute;left:109px;top:47px;font-size:10px;line-height:13px;color:var(--slate);width:135px}
.card a{position:absolute;left:109px;top:80px;font-size:10px;color:var(--slate)}

/* featured */
.featured{left:0;top:589px;width:800px;height:376px;background:#fff}
.prod{position:absolute;width:250px;height:150px}
.prod .jar{position:absolute;left:0;top:0;width:60px;height:120px;border-radius:8px}
.prod .name{position:absolute;left:81px;top:6px;font-size:11.5px;color:var(--slate)}
.prod .type{position:absolute;left:81px;top:20px;font-size:11px;color:#222}
.prod .desc{position:absolute;left:81px;top:37px;width:140px;font-size:10px;line-height:13px;color:var(--muted);text-align:justify;text-align-last:justify}
.prod .cart{position:absolute;left:81px;top:82px;width:106px;height:22px;background:linear-gradient(#5e9a26,var(--green-dark));border-radius:3px;color:#fff;font-size:10px;line-height:22px;padding-left:27px;box-shadow:1px 1px 2px #999}
.prod .cart svg{position:absolute;left:9px;top:5px}
.prod .more{position:absolute;left:84px;top:116px;font-size:10px;color:var(--pink);text-decoration:underline}
.jar-white{background:linear-gradient(90deg,#d8dde3,#ffffff 45%,#dfe4ea)}
.jar-red{background:linear-gradient(180deg,#ffffff 0%,#f3f3f3 20%,#b52034 45%,#f2f2f2 80%,#7a1b28 100%)}
.jar-blue{background:linear-gradient(180deg,#1f2e6e 0%,#2c4a9c 20%,#ecf0f6 45%,#e8ecf3 70%,#1f3f8f 100%)}

/* footer */
.footer{left:0;top:965px;width:800px;height:183px;background:var(--footer)}
.fcol{position:absolute;top:17px}
.fcol h5{font-size:12px;font-weight:600;color:#333;margin-bottom:11px}
.fcol li{list-style:none;font-size:10px;color:#6f7a84;height:17.6px}
.social{position:absolute;width:26px;height:26px;background:var(--slate-dark);border-radius:2px;box-shadow:1px 1px 1px #aaa}
.bottom{left:0;top:1148px;width:800px;height:30px;background:var(--slate);color:#fff;font-size:10px;line-height:30px;padding:0 19px;display:flex;justify-content:space-between}
</style>
</head>
<body>
<div class="page">

  <header>
    <div class="abs brand"><span class="brand-mark"></span><span class="brand-name">velomira</span></div>
    <div class="abs vsep" style="left:262px;top:22px"></div>
    <svg class="abs" style="left:276px;top:21px" width="28" height="20" viewBox="0 0 28 20" aria-hidden="true">
      <rect x="1" y="3" width="16" height="11" fill="#8da1b3"/><path d="M17 6h6l4 4v4H17z" fill="#6b869d"/>
      <circle cx="6" cy="16" r="2.5" fill="#56708a"/><circle cx="22" cy="16" r="2.5" fill="#56708a"/>
    </svg>
    <div class="abs info" style="left:315px;top:16px">18 Std. Lieferung<br>in der Schweiz</div>
    <div class="abs info" style="left:427px;top:16px">Gratisversand<br>ab 80 CHF</div>
    <div class="abs vsep" style="left:509px;top:18px;height:30px"></div>
    <svg class="abs" style="left:520px;top:17px" width="25" height="25" viewBox="0 0 25 25" aria-hidden="true">
      <circle cx="12.5" cy="12.5" r="12" fill="#6b869d"/><text x="12.5" y="18" text-anchor="middle" font-family="Open Sans,sans-serif" font-size="15" font-weight="700" fill="#fff">?</text>
    </svg>
    <div class="abs info" style="left:554px;top:16px">Experten<br>Beratung</div>
    <div class="abs vsep" style="left:610px;top:22px"></div>
    <div class="abs search">Search
      <svg width="11" height="11" viewBox="0 0 11 11" aria-hidden="true"><circle cx="4.5" cy="4.5" r="3.5" stroke="#777" stroke-width="1.5" fill="none"/><path d="M7 7l3 3" stroke="#777" stroke-width="1.5"/></svg>
    </div>
    <div class="abs topright" style="top:9px">Welcome to our site</div>
    <div class="abs topright" style="top:34px">Shopping Cart: <span class="items">0 items</span></div>
    <div class="abs topright" style="top:58px">My Account I Help I
      <svg class="flag" viewBox="0 0 3 3" preserveAspectRatio="none"><rect width="3" height="1" fill="#000"/><rect y="1" width="3" height="1" fill="#d00"/><rect y="2" width="3" height="1" fill="#fc0"/></svg>
      <svg class="flag" viewBox="0 0 3 3" preserveAspectRatio="none"><rect width="1" height="3" fill="#0a3d9c"/><rect x="1" width="1" height="3" fill="#fff"/><rect x="2" width="1" height="3" fill="#e0202a"/></svg>
    </div>
  </header>

  <nav class="abs nav">
    <a style="left:29px">HOME</a><i style="left:81px"></i>
    <a style="left:97px">ABOUT</a><i style="left:150px"></i>
    <a style="left:169px">PRODUCTS</a><i style="left:234px"></i>
    <a style="left:247px">CUSTOMER SERVICE</a><i style="left:361px"></i>
    <a style="left:384px">SITE MAP</a><i style="left:446px"></i>
    <a style="left:469px">SEARCH TERMS</a><i style="left:560px"></i>
    <a style="left:582px">ADVANCED SEARCH</a><i style="left:690px"></i>
    <a style="left:718px">CONTACTS</a>
  </nav>

  <section class="abs hero">
    <div class="abs cats">
      <h3>CATEGORIES</h3>
      <ul>
        <li>Categories Links 1</li><li>Categories Links 2</li><li>Categories Links 3</li><li>Categories Links 4</li><li>Categories Links 5</li>
        <li>Categories Links 6</li><li>Categories Links 7</li><li>Categories Links 8</li><li>Categories Links 9</li><li>Categories Links 10</li>
      </ul>
    </div>
    <div class="abs slide">
      <div class="abs slide-photo" role="img" aria-label="Product photo of a blue supplement bottle"></div>
      <h2 class="abs">Lorem ipsum dolor sit amet</h2>
      <p class="abs">Ut sem turpis, venenatis vel laoreet et, pellen-tesque quis nunc. Fusce feugiat vulputate tincid-unt. Vestibulum ante ipsum primis in faucibus orci luctus et ultrices posuere cubilia Curae;</p>
      <div class="abs btn-shop">SHOP NOW</div>
      <div class="abs dots"><span></span><span></span><span class="on"></span><span></span><span></span></div>
    </div>
    <aside class="abs help">
      <div class="abs help-photo" role="img" aria-label="Photo of a customer service agent with headset"></div>
      <h3 class="abs">Customer Help</h3>
      <div class="abs phone">555 - 210<br>-3846</div>
      <div class="abs click">CLICK HERE</div>
    </aside>
  </section>

  <section class="abs special">
    <h2 class="sec-title">SPECIAL PRODUCTS</h2>
    <div class="sec-rule" style="top:41px"></div>
    <div class="card" style="left:16px">
      <div class="pack" role="img" aria-label="Product box, blue and white" style="background:linear-gradient(135deg,#1e3f8f 0%,#f4f6fa 30%,#ffffff 70%,#d6dbe6 100%)"></div>
      <h4 style="color:#222">Aenean ac neque quam.</h4>
      <p>Pellentesque posuere metus sit amet odio</p>
      <a>Click Here</a>
    </div>
    <div class="card" style="left:276px">
      <div class="pack" role="img" aria-label="Product box, pink and white" style="background:linear-gradient(135deg,#c2185b 0%,#f8e3ee 30%,#ffffff 70%,#e6d6de 100%)"></div>
      <h4 style="color:var(--crimson)">Aenean ac neque quam.</h4>
      <p>Pellentesque posuere metus sit amet odio</p>
      <a>Click Here</a>
    </div>
    <div class="card" style="left:535px">
      <div class="pack" role="img" aria-label="Product box, orange and white" style="background:linear-gradient(135deg,#e8571a 0%,#fbe8d8 30%,#ffffff 70%,#e3e3e3 100%)"></div>
      <h4 style="color:var(--orange-red)">Aenean ac neque quam.</h4>
      <p>Pellentesque posuere metus sit amet odio</p>
      <a>Click Here</a>
    </div>
  </section>

  <section class="abs featured">
    <h2 class="sec-title">FEATURED PRODUCTS</h2>
    <div class="sec-rule" style="top:41px"></div>

    <div class="prod" style="left:36px;top:64px">
      <div class="jar jar-white" role="img" aria-label="White supplement tub"></div>
      <div class="name">Product Name</div><div class="type">Product Type</div>
      <div class="desc">Quis autem vel eum iure reprehen derit qui in ea voluptate velit esse quam</div>
      <div class="cart"><svg width="12" height="11" viewBox="0 0 12 11"><path d="M0 1h2l2 6h6l1.5-4H3" stroke="#fff" stroke-width="1.3" fill="none"/><circle cx="5" cy="9.5" r="1.1" fill="#fff"/><circle cx="9" cy="9.5" r="1.1" fill="#fff"/></svg>ADD TO CART</div>
      <a class="more">More Info</a>
    </div>
    <div class="prod" style="left:294px;top:64px">
      <div class="jar jar-red" role="img" aria-label="White bottle with red fruit label"></div>
      <div class="name" style="left:80px">Product Name</div><div class="type" style="left:80px">Product Type</div>
      <div class="desc" style="left:80px">Quis autem vel eum iure reprehen derit qui in ea voluptate velit esse quam</div>
      <div class="cart" style="left:80px"><svg width="12" height="11" viewBox="0 0 12 11"><path d="M0 1h2l2 6h6l1.5-4H3" stroke="#fff" stroke-width="1.3" fill="none"/><circle cx="5" cy="9.5" r="1.1" fill="#fff"/><circle cx="9" cy="9.5" r="1.1" fill="#fff"/></svg>ADD TO CART</div>
      <a class="more" style="left:83px">More Info</a>
    </div>
    <div class="prod" style="left:550px;top:64px">
      <div class="jar jar-blue" role="img" aria-label="Blue supplement bottle"></div>
      <div class="name" style="left:80px">Product Name</div><div class="type" style="left:80px">Product Type</div>
      <div class="desc" style="left:80px">Quis autem vel eum iure reprehen derit qui in ea voluptate velit esse quam</div>
      <div class="cart" style="left:80px"><svg width="12" height="11" viewBox="0 0 12 11"><path d="M0 1h2l2 6h6l1.5-4H3" stroke="#fff" stroke-width="1.3" fill="none"/><circle cx="5" cy="9.5" r="1.1" fill="#fff"/><circle cx="9" cy="9.5" r="1.1" fill="#fff"/></svg>ADD TO CART</div>
      <a class="more" style="left:83px">More Info</a>
    </div>

    <div class="prod" style="left:36px;top:227px">
      <div class="jar jar-white" role="img" aria-label="White supplement tub"></div>
      <div class="name">Product Name</div><div class="type">Product Type</div>
      <div class="desc">Quis autem vel eum iure reprehen derit qui in ea voluptate velit esse quam</div>
      <div class="cart"><svg width="12" height="11" viewBox="0 0 12 11"><path d="M0 1h2l2 6h6l1.5-4H3" stroke="#fff" stroke-width="1.3" fill="none"/><circle cx="5" cy="9.5" r="1.1" fill="#fff"/><circle cx="9" cy="9.5" r="1.1" fill="#fff"/></svg>ADD TO CART</div>
      <a class="more">More Info</a>
    </div>
    <div class="prod" style="left:294px;top:227px">
      <div class="jar jar-red" role="img" aria-label="White bottle with red fruit label"></div>
      <div class="name" style="left:80px">Product Name</div><div class="type" style="left:80px">Product Type</div>
      <div class="desc" style="left:80px">Quis autem vel eum iure reprehen derit qui in ea voluptate velit esse quam</div>
      <div class="cart" style="left:80px"><svg width="12" height="11" viewBox="0 0 12 11"><path d="M0 1h2l2 6h6l1.5-4H3" stroke="#fff" stroke-width="1.3" fill="none"/><circle cx="5" cy="9.5" r="1.1" fill="#fff"/><circle cx="9" cy="9.5" r="1.1" fill="#fff"/></svg>ADD TO CART</div>
      <a class="more" style="left:83px">More Info</a>
    </div>
    <div class="prod" style="left:550px;top:227px">
      <div class="jar jar-blue" role="img" aria-label="Blue supplement bottle"></div>
      <div class="name" style="left:80px">Product Name</div><div class="type" style="left:80px">Product Type</div>
      <div class="desc" style="left:80px">Quis autem vel eum iure reprehen derit qui in ea voluptate velit esse quam</div>
      <div class="cart" style="left:80px"><svg width="12" height="11" viewBox="0 0 12 11"><path d="M0 1h2l2 6h6l1.5-4H3" stroke="#fff" stroke-width="1.3" fill="none"/><circle cx="5" cy="9.5" r="1.1" fill="#fff"/><circle cx="9" cy="9.5" r="1.1" fill="#fff"/></svg>ADD TO CART</div>
      <a class="more" style="left:83px">More Info</a>
    </div>
  </section>

  <footer class="abs footer">
    <div class="fcol" style="left:38px"><h5>Information</h5><ul>
      <li>About Us</li><li>Customer Service</li><li>Privacy Policy</li><li>Site Map</li><li>Search Terms</li><li>Orders and Returns</li><li>Contact Us</li></ul></div>
    <div class="fcol" style="left:238px"><h5>Why buy from us</h5><ul>
      <li>Shipping &amp; Returns</li><li>Secure Shopping</li><li>International Shipping</li><li>Affiliates</li><li>Group Sales</li></ul></div>
    <div class="fcol" style="left:454px"><h5>My account</h5><ul>
      <li>Sign In</li><li>View Cart</li><li>My Wishlist</li><li>Track My Order</li><li>Help</li></ul></div>
    <div class="fcol" style="left:632px"><h5>Socialize with us</h5></div>
    <span class="social" style="left:632px;top:44px"></span>
    <span class="social" style="left:670px;top:44px"></span>
    <span class="social" style="left:708px;top:44px"></span>
    <span class="social" style="left:632px;top:79px"></span>
    <span class="social" style="left:670px;top:79px"></span>
    <span class="social" style="left:708px;top:79px"></span>
  </footer>

  <div class="abs bottom"><span>Copyright © 2012 | Velomira | All Rights Reserved</span><span>M3</span></div>
</div>
</body>
</html>
```